Letterhead and Corporate Stationary Design Project

I would like the following designed:
1. Corporate Letterhead
2. Compliment Slips
3. Business Cards(2)

I have attached word document that outlines the text to be contained for all 3. The logo is fine as is and can be used in the design.
I only need letterhead to be designed for contest, the successful applicant can desisgn other 2 items after being awarded the job

Target Market(s)

Information Technology

Industry/Entity Type

Business

Requirements
Must have
• Border around entire letter that matches colours in logo
Clearly identifiable letterhead and footer
Nice to have
• Watermark

```html
<!DOCTYPE html>
<html lang="en">
<head>
<meta charset="utf-8">
<title>Veltora Business Solutions – Stationery Set</title>
<link rel="stylesheet" href="https://fonts.googleapis.com/css2?family=Tinos:wght@400;700&display=swap">
<style>
  :root {
    --backdrop: #80868e;
    --paper: #ffffff;
    --navy: #0b3a85;
    --blue: #1d8fd6;
    --sky: #5cc3ee;
    --pale: #dcecf7;
    --ink: #555a60;
    --window: #e4e6e8;
  }
  * { box-sizing: border-box; margin: 0; padding: 0; }
  html, body { width: 1200px; height: 898px; overflow: hidden; }
  body {
    background: var(--backdrop);
    font-family: "Tinos", "Times New Roman", serif;
    position: relative;
  }
  address { font-style: normal; }
  .sheet { position: absolute; background: var(--paper); overflow: hidden; }

  /* brand name block */
  .brand { position: absolute; display: flex; align-items: center; gap: 6px; }
  .brand__dot { width: 16px; height: 16px; border-radius: 50%; background: var(--blue); flex: none; }
  .brand__name { font-weight: 700; color: var(--navy); line-height: 1; white-space: nowrap; }

  .address {
    position: absolute; text-align: right; color: var(--navy);
    font-weight: 700; font-size: 8.6px; line-height: 9.6px;
  }

  /* folder */
  .folder { left: 149px; top: 78px; width: 424px; height: 565px; }
  .folder__sweep { position: absolute; inset: 0; }
  .folder .brand { right: 42px; top: 32px; }
  .folder .brand__dot { width: 26px; height: 26px; }
  .folder .brand__name { font-size: 21px; }
  .folder__art {
    position: absolute; left: 96px; top: 268px; width: 320px; height: 265px;
    background: radial-gradient(ellipse at 45% 40%, #a9d6f0 0%, #b9c6dc 45%, rgba(205,215,228,0) 75%);
  }

  /* letterhead */
  .letterhead { left: 620px; top: 78px; width: 381px; height: 531px; }
  .band { position: absolute; left: 0; right: 0; background: linear-gradient(90deg, var(--pale) 0%, var(--sky) 35%, var(--blue) 70%, var(--navy) 100%); }
  .letterhead__top { top: 0; height: 12px; }
  .letterhead__bottom { bottom: 0; height: 11px; }
  .letterhead .brand { left: 30px; top: 44px; }
  .letterhead .brand__name { font-size: 15px; }
  .letterhead .address { right: 16px; top: 20px; }
  .letterhead__watermark {
    position: absolute; right: 20px; bottom: 28px; width: 165px; height: 110px;
    background: radial-gradient(ellipse at 55% 50%, rgba(170,205,235,0.45) 0%, rgba(210,225,240,0.25) 55%, rgba(255,255,255,0) 80%);
  }
  .letter {
    position: absolute; left: 66px; top: 110px; width: 290px;
    font-size: 5.6px; line-height: 8.7px; color: var(--ink);
  }
  .letter p { margin-bottom: 8.7px; }
  .letter ul { list-style: none; padding-left: 4px; margin-bottom: 8.7px; }
  .letter__date { margin-bottom: 17px !important; }
  .letter__sign { margin-top: 17px; }
  .letter__name { margin-top: 17px; }
  .footer-legal {
    position: absolute; right: 18px; bottom: 20px; text-align: right;
    color: var(--navy); font-weight: 700; font-size: 8.4px; line-height: 10px;
  }

  /* business card front */
  .card-front { left: 138px; top: 673px; width: 223px; height: 127px; }
  .card-front .brand { left: 10px; top: 22px; gap: 4px; align-items: flex-start; }
  .card-front .brand__dot { width: 10px; height: 10px; margin-top: 1px; }
  .card-front .brand__name { font-size: 8px; line-height: 9px; }
  .card-front .address { right: 129px; top: 46px; font-size: 6.4px; line-height: 7.2px; }
  .card-front__rule { position: absolute; left: 100px; top: 30px; width: 1px; height: 66px; background: #9aa3ad; }
  .card-front__person { position: absolute; left: 108px; top: 31px; width: 110px; text-align: center; color: #222; }
  .card-front__name { font-size: 10px; letter-spacing: 0.6px; line-height: 12px; }
  .card-front__role { font-size: 10px; line-height: 12px; }
  .card-front__contact { position: absolute; left: 116px; top: 67px; font-size: 6.6px; line-height: 9px; color: #222; }

  /* business card back */
  .card-back {
    left: 367px; top: 673px; width: 224px; height: 127px;
    background: radial-gradient(ellipse at 50% 45%, #c9ecfb 0%, #5fc3ef 45%, #1f8fd4 100%);
  }
  .card-back__art {
    position: absolute; left: 52px; top: 22px; width: 118px; height: 86px;
    background: radial-gradient(ellipse at 50% 45%, #1a6cc2 0%, #3a78b8 45%, rgba(120,160,200,0) 78%);
  }

  /* envelope */
  .envelope { left: 620px; top: 625px; width: 451px; height: 220px; }
  .envelope .brand { left: 24px; top: 70px; }
  .envelope .brand__name { font-size: 15px; }
  .envelope .address { left: 60px; width: 64px; top: 96px; text-align: right; font-size: 6.8px; line-height: 7.6px; }
  .envelope__phone { position: absolute; left: 70px; top: 145px; font-size: 6.8px; line-height: 7.6px; color: var(--navy); font-weight: 700; }
  .envelope__watermark {
    position: absolute; left: 190px; top: 0; width: 261px; height: 220px;
    background: radial-gradient(ellipse at 55% 45%, rgba(205,225,242,0.85) 0%, rgba(228,236,244,0.55) 50%, rgba(255,255,255,0) 80%);
  }
  .envelope__window {
    position: absolute; left: 262px; top: 122px; width: 155px; height: 70px;
    border-radius: 8px; background: var(--window);
  }
</style>
</head>
<body>

  <!-- presentation folder -->
  <section class="sheet folder" aria-label="Presentation folder">
    <svg class="folder__sweep" viewBox="0 0 424 565" preserveAspectRatio="none" aria-hidden="true">
      <defs>
        <linearGradient id="sweepFill" x1="0" y1="1" x2="1" y2="0">
          <stop offset="0" stop-color="#0a3f86"/>
          <stop offset="0.35" stop-color="#1d8fd6"/>
          <stop offset="0.6" stop-color="#7fd0f2"/>
          <stop offset="1" stop-color="#ffffff" stop-opacity="0"/>
        </linearGradient>
      </defs>
      <path d="M0 60 C 40 200, 60 420, 150 565 L 0 565 Z" fill="url(#sweepFill)"/>
      <path d="M0 140 C 60 260, 110 430, 230 565 L 150 565 C 60 420, 40 200, 0 60 Z" fill="#5cc3ee" opacity="0.35"/>
    </svg>
    <div class="brand">
      <span class="brand__dot"></span>
      <span class="brand__name">Veltora Business Solutions</span>
    </div>
    <div class="folder__art" role="img" aria-label="Large three-dimensional cog illustration in light blue and grey"></div>
  </section>

  <!-- letterhead -->
  <section class="sheet letterhead" aria-label="Letterhead">
    <div class="band letterhead__top"></div>
    <div class="letterhead__watermark" role="img" aria-label="Faint cog watermark"></div>
    <div class="brand">
      <span class="brand__dot"></span>
      <span class="brand__name">Veltora Business Solutions</span>
    </div>
    <address class="address">
      Weir House<br>8 Mill Lane<br>Trim<br>Co. Louth<br>Ireland<br><br>+ 353 41 5550184<br>www.veltora.ie
    </address>

    <article class="letter">
      <p class="letter__date">October 18, 2012</p>
      <p>Re : Director of Business Development</p>
      <p>Building corporate value is my expertise. Whether challenged to orchestrate an aggressive turnaround, accelerate growth, or provide day to day operating leadership, I have consistently delivered strong financial result. My record of success has been predicated upon establishing a clear vision statement and then following through with thoughtful, deliberate strategic planning.</p>
      <p>Currently, I am President and CEO of Veltora, a $113M division that develops energy saving LED systems. During my tenure, the division's significant revenue and profit growth can be attributed to my strong leadership, sound strategic planning and expert negotiating ability.</p>
      <p style="margin-bottom:0">In 2 years, I have :</p>
      <ul>
        <li>- Accelerated enterprise growth 300%.</li>
        <li>- Increased sales 200% and boosted net income 400%.</li>
        <li>- Raised net cash position 350%.</li>
        <li>- Added 250 international clients.</li>
        <li>- Generated $1.5M in cost savings</li>
      </ul>
      <p>These milestones were achieved by orchestrating aggressive channel development initiatives, structuring and negotiating strategic alliances and spearheading expansion within high growth, global market. Time and again I have recognized new market opportunities, conceived of strategies to capitalize on these opportunities and developed a clear path to success.</p>
      <p>While secure in my current position, I am confidentially seeking an opportunity to expand my range of leadership abilities in a top level management position with an organization seeking to expand revenue positions and achieve market dominance. I'd like to meet to discuss ways in which my management expertise can be of value to your organization. I will call you within the week to schedule a conversation.</p>
      <p class="letter__sign">Sincerely,</p>
      <p class="letter__name">Dermot Kealy.</p>
    </article>

    <div class="footer-legal">
      Veltora Business Solutions Limited<br>Company Registration 517394<br>VAT No IE5173940K
    </div>
    <div class="band letterhead__bottom"></div>
  </section>

  <!-- business card, front -->
  <section class="sheet card-front" aria-label="Business card front">
    <div class="brand">
      <span class="brand__dot"></span>
      <span class="brand__name">Veltora<br>Business Solutions</span>
    </div>
    <address class="address">
      Weir House<br>8 Mill Lane<br>Trim<br>Co. Louth<br>Ireland<br>www.veltora.ie
    </address>
    <div class="card-front__rule"></div>
    <div class="card-front__person">
      <div class="card-front__name">DERMOT KEALY</div>
      <div class="card-front__role">CEO</div>
    </div>
    <div class="card-front__contact">
      P. 353 41 5550267<br>M. 353 87 5550391<br>email : dkealy@veltora.ie
    </div>
  </section>

  <!-- business card, back -->
  <section class="sheet card-back" aria-label="Business card back">
    <div class="card-back__art" role="img" aria-label="Cluster of three-dimensional cogs in blue, navy and grey"></div>
  </section>

  <!-- envelope -->
  <section class="sheet envelope" aria-label="DL envelope">
    <div class="envelope__watermark" role="img" aria-label="Faint cog watermark"></div>
    <div class="envelope__window"></div>
    <div class="brand">
      <span class="brand__dot"></span>
      <span class="brand__name">Veltora Business Solutions</span>
    </div>
    <address class="address">
      Weir House<br>8 Mill Lane<br>Trim<br>Co. Louth<br>Ireland
    </address>
    <div class="envelope__phone">+ 353 41 5550184<br>www.veltora.ie</div>
  </section>

</body>
</html>
```